Global HR Recruitment firm looking to update PPT deck

We have been using our current format of powerpoint for 3-4 years. It serves its purpose but could do with modernising and giving users the ability to showcase elements of the business in a more graphic manner.

To help with this I have included the current deck which can you see through the master template files and created a list of elements we would like to have added into the deck. The idea is for us to have additional layouts that we can then drop in content relevant to the client we are taking to.

You can see more about our company at veltranhq.com

The brand guidelines are attached. However we are open to adaptation - but fonts and logos cannot change

Our main font is Sofia Pro

Main colour palette for reference - though we are happy to consider broader colour options
Dark Blue 00205B
Navy Blue 25338D
Turqoise A1D4EC
Yellow FFDA21
Light Gray A0A4BE
Cyan 0FC5C4

Target Market(s)

Senior Professionals in top tier brands

Industry/Entity Type

All

Font styles to use
Other font styles liked:
• Please see brand guidelines

Colors
0054AA
0677BA
7BADD7
CADEEF
E8F1F8
0094D4
00A9DD
6FCCEA
C7EBF8
E9F6FB
00AB8E
00BBA5
67D7C9
C6EFE9
E9F9F6
FFF300
FFF600
FEFA6F
FFFEC7
FFFEE8
E54698
E96AAD
F1A4CE
F9D9EA
FCEFF6

Requirements
Should not have
• Cartoon imagery

```html
<!DOCTYPE html>
<html lang="en">
<head>
<meta charset="utf-8">
<title>Veltran Presentation Deck</title>
<link href="https://fonts.googleapis.com/css2?family=Roboto:wght@300;400;500;700;900&display=swap" rel="stylesheet">
<style>
:root{
  --bg:#8e8e90;
  --dark:#00205b;
  --blue:#0054aa;
  --mid:#0677ba;
  --sky:#0094d4;
  --cyan:#00a9dd;
  --pale:#e8f1f8;
  --pale2:#cadeef;
  --ink:#1d2433;
  --grey:#7a8092;
  --line:#d5dde8;
  --white:#ffffff;
  --teal:#00bba5;
  --pink:#e54698;
  --yellow:#ffda21;
}
*{box-sizing:border-box;margin:0;padding:0}
html,body{width:1200px;height:2248px;overflow:hidden}
body{background:var(--bg);font-family:"Roboto",Arial,sans-serif;color:var(--ink)}
.board{width:1200px;height:2248px;padding:0 40px;display:grid;grid-template-columns:545px 545px;grid-auto-rows:307px;gap:40px 30px;align-content:center}
.slide{position:relative;background:var(--white);overflow:hidden;box-shadow:0 4px 14px rgba(0,0,0,.18)}
.brand{position:absolute;top:12px;right:16px;font-weight:700;font-size:14px;color:var(--blue);display:flex;align-items:center;gap:5px}
.brand i{width:8px;height:8px;border-radius:50%;background:var(--sky);display:block}
.foot{position:absolute;left:0;right:0;bottom:0;height:6px;background:linear-gradient(90deg,var(--blue),var(--cyan))}
.title{position:absolute;left:26px;top:22px;font-size:22px;font-weight:700;color:var(--dark)}
.title span{color:var(--sky)}
.photo{position:absolute;background:linear-gradient(135deg,#c7d3e2,#8fa7c4)}
.small{font-size:7.5px;line-height:1.45;color:var(--grey)}
/* slide 1 */
.cover-panel{position:absolute;left:0;top:0;bottom:0;width:300px;background:linear-gradient(160deg,var(--blue),var(--sky))}
.cover-panel .brand{left:26px;top:50px;right:auto;color:var(--white);font-size:24px}
.cover-panel .brand i{background:var(--white);width:12px;height:12px}
.cover-panel h1{position:absolute;left:26px;top:100px;width:250px;font-size:19px;line-height:1.25;color:var(--white);font-weight:700}
.cover-panel .pill{position:absolute;left:26px;top:172px;background:var(--white);color:var(--blue);font-size:8px;font-weight:500;padding:5px 12px;border-radius:10px}
/* slide 2 */
.deck-cards{position:absolute;left:150px;right:20px;top:110px;display:grid;grid-template-columns:repeat(3,1fr);gap:12px}
.card{border:1px solid var(--line);border-radius:6px;padding:32px 10px 12px;text-align:center;position:relative;height:130px}
.card .ic{position:absolute;top:-16px;left:50%;margin-left:-16px;width:32px;height:32px;border-radius:50%;background:var(--sky);display:flex;align-items:center;justify-content:center}
.card p{font-size:8.5px;color:var(--ink);line-height:1.5}
/* slide 3 */
.info-list{position:absolute;left:200px;top:70px;right:30px;list-style:none}
.info-list li{font-size:8px;line-height:1.5;color:var(--grey);margin-bottom:9px;padding-left:12px;position:relative}
.info-list li::before{content:"";position:absolute;left:0;top:4px;width:5px;height:5px;border-radius:50%;background:var(--sky)}
.info-list b{color:var(--dark);font-weight:500}
/* slide 4 */
.hub{position:absolute;left:30px;top:100px;width:100px;height:100px;border-radius:50%;background:var(--blue);color:var(--white);font-weight:700;font-size:15px;display:flex;align-items:center;justify-content:center;border:6px solid var(--pale2)}
.node{position:absolute;left:200px;width:145px;border:1px solid var(--line);border-radius:4px;padding:6px 8px}
.node h4{font-size:8.5px;color:var(--white);background:var(--mid);padding:3px 6px;border-radius:2px;margin:-6px -8px 5px}
.tag{position:absolute;left:370px;width:150px;height:18px;border-radius:3px;background:var(--pale);font-size:7.5px;color:var(--dark);padding:4px 8px}
/* slide 5 */
.steps{position:absolute;left:22px;right:22px;top:110px;display:flex;gap:4px}
.step{flex:1;height:56px;background:var(--sky);color:var(--white);font-size:22px;font-weight:700;display:flex;align-items:center;justify-content:center;clip-path:polygon(0 0,86% 0,100% 50%,86% 100%,0 100%,12% 50%)}
.step:nth-child(2){background:var(--mid)}.step:nth-child(3){background:var(--blue)}.step:nth-child(4){background:var(--cyan)}.step:nth-child(5){background:#6fccea}
.step-text{position:absolute;left:22px;right:22px;top:182px;display:flex;gap:4px}
.step-text div{flex:1;padding:0 6px}
.step-text b{display:block;font-size:8.5px;color:var(--dark);margin-bottom:3px}
/* slide 6 */
.industries{position:absolute;left:22px;right:22px;top:90px;display:flex;justify-content:space-between}
.ind{width:72px;text-align:center}
.ring{width:54px;height:54px;border-radius:50%;border:3px solid var(--sky);margin:0 auto 8px;display:flex;align-items:center;justify-content:center}
.ring i{width:18px;height:18px;border:2px solid var(--sky);border-radius:3px;display:block}
.ind h5{font-size:8px;font-weight:500;color:var(--ink)}
.ind strong{display:block;font-size:17px;color:var(--dark);margin-top:3px}
/* slide 7 */
.team-cards{position:absolute;left:22px;right:22px;top:170px;display:grid;grid-template-columns:repeat(4,1fr);gap:8px}
.tcard{height:110px;border-radius:4px;padding:10px}
.tcard h5{font-size:9px;margin-bottom:5px}
.tcard.light{background:var(--pale)}.tcard.light h5{color:var(--dark)}
.tcard.dark{background:var(--blue)}.tcard.dark h5,.tcard.dark .small{color:var(--white)}
/* slide 8 */
.profile{position:absolute;left:290px;top:70px;right:20px}
.profile .who{display:flex;gap:10px;align-items:center}
.avatar{width:44px;height:44px;border-radius:50%;background:linear-gradient(135deg,#c7d3e2,#8fa7c4)}
.who h4{font-size:12px;color:var(--dark)}
.who p{font-size:8px;color:var(--grey)}
.contact{margin-top:12px;list-style:none}
.contact li{font-size:8px;color:var(--ink);display:flex;align-items:center;gap:6px;margin-bottom:6px}
.quote{margin-top:10px;background:var(--blue);color:var(--white);font-size:8.5px;line-height:1.5;padding:10px 12px;border-radius:4px}
</style>
</head>
<body>
<main class="board">

  <!-- Cover -->
  <section class="slide">
    <div class="cover-panel">
      <div class="brand"><i></i>Veltran</div>
      <h1>Connecting Global Business Leaders with World-Class HR Talent</h1>
      <div class="pill">veltranhq.com</div>
    </div>
    <div class="photo" role="img" aria-label="Hand holding a phone showing a pastel beach horizon" style="left:300px;top:0;right:0;bottom:0;background:linear-gradient(180deg,#dfe9f4,#b9cbe6 45%,#e7c7d6 70%,#9ab6d8)"></div>
  </section>

  <!-- Main deck -->
  <section class="slide">
    <div class="brand"><i></i>Veltran</div>
    <div class="photo" role="img" aria-label="Business meeting photo in a circle" style="left:-30px;top:-30px;width:160px;height:160px;border-radius:50%"></div>
    <div class="title" style="left:200px;top:34px;font-size:17px;text-align:center;width:230px">This is the main Veltran<br><span>presentation deck</span></div>
    <div class="deck-cards">
      <div class="card"><div class="ic"><svg width="14" height="14" viewBox="0 0 14 14"><path d="M2 7l3 3 7-7" stroke="#fff" stroke-width="2" fill="none"/></svg></div><p>We offer 'Quick guidance for our clients' needs in one place</p></div>
      <div class="card"><div class="ic"><svg width="14" height="14" viewBox="0 0 14 14"><circle cx="7" cy="7" r="5" stroke="#fff" stroke-width="2" fill="none"/></svg></div><p>We take time to listen and build a clear picture of each role</p></div>
      <div class="card"><div class="ic"><svg width="14" height="14" viewBox="0 0 14 14"><path d="M2 7h10M8 3l4 4-4 4" stroke="#fff" stroke-width="2" fill="none"/></svg></div><p>We are genuinely open to suggestions of options and additions</p></div>
    </div>
    <div class="foot"></div>
  </section>

  <!-- General information -->
  <section class="slide">
    <div class="brand"><i></i>Veltran</div>
    <div class="photo" role="img" aria-label="Blue-tinted office photo" style="left:0;top:0;bottom:0;width:170px;background:linear-gradient(160deg,var(--blue),var(--sky))"></div>
    <div class="title" style="left:200px;top:22px">General <span>information</span></div>
    <ul class="info-list">
      <li><b>Who we are</b> – A global executive search partner focused on senior HR talent.</li>
      <li><b>Our reach</b> – Offices and associates across the Americas, Europe and Asia Pacific.</li>
      <li><b>Our clients</b> – Leading brands seeking proven people leaders.</li>
      <li><b>How we work</b> – Research-led search, clear updates and a shortlist built on fit.</li>
      <li><b>Next steps</b> – Agree the brief, timeline and key success measures.</li>
    </ul>
    <div class="foot"></div>
  </section>

  <!-- Process diagram -->
  <section class="slide">
    <div class="brand"><i></i>Veltran</div>
    <div class="hub">Veltran</div>
    <svg width="545" height="307" style="position:absolute;left:0;top:0" aria-hidden="true">
      <path d="M142 150 H175 M175 70 V240 M175 70 H200 M175 150 H200 M175 240 H200 M345 70 H370 M345 150 H370 M345 240 H370" stroke="#0677ba" stroke-width="1.2" fill="none"/>
    </svg>
    <div class="node" style="top:50px"><h4>Research</h4><p class="small">Market map and target list</p></div>
    <div class="node" style="top:130px"><h4>Shortlist</h4><p class="small">Interviews and assessment</p></div>
    <div class="node" style="top:220px"><h4>Placement</h4><p class="small">Offer, onboarding, follow-up</p></div>
    <div class="tag" style="top:61px">Week 1–3</div>
    <div class="tag" style="top:141px">Week 4–6</div>
    <div class="tag" style="top:231px">Week 7–10</div>
    <div class="foot"></div>
  </section>

  <!-- Status summary -->
  <section class="slide">
    <div class="brand"><i></i>Veltran</div>
    <div class="title">Status summary by <span>progress</span></div>
    <div class="steps"><div class="step">02</div><div class="step">02</div><div class="step">02</div><div class="step">01</div><div class="step">25</div></div>
    <div class="step-text">
      <div><b>Offers</b><p class="small">Pending final sign-off</p></div>
      <div><b>Finals</b><p class="small">Meeting the panel</p></div>
      <div><b>Shortlist</b><p class="small">Under client review</p></div>
      <div><b>Longlist</b><p class="small">Being assessed</p></div>
      <div><b>Contacted</b><p class="small">Initial outreach</p></div>
    </div>
    <div class="foot"></div>
  </section>

  <!-- Candidate industry -->
  <section class="slide">
    <div class="brand"><i></i>Veltran</div>
    <div class="title" style="left:0;right:0;text-align:center;top:30px">Candidate Current <span>Industry</span></div>
    <div class="industries">
      <div class="ind"><div class="ring"><i></i></div><h5>Consumer</h5><strong>7%</strong></div>
      <div class="ind"><div class="ring"><i></i></div><h5>Education</h5><strong>2%</strong></div>
      <div class="ind"><div class="ring"><i></i></div><h5>Energy</h5><strong>1%</strong></div>
      <div class="ind"><div class="ring"><i></i></div><h5>Finance</h5><strong>7%</strong></div>
      <div class="ind"><div class="ring"><i></i></div><h5>Retail</h5><strong>1%</strong></div>
      <div class="ind"><div class="ring"><i></i></div><h5>Technology</h5><strong>4%</strong></div>
    </div>
    <div class="foot"></div>
  </section>

  <!-- Title goes here -->
  <section class="slide">
    <div class="brand"><i></i>Veltran</div>
    <div class="title" style="font-size:18px">Title Goes Here</div>
    <p class="small" style="position:absolute;left:26px;top:54px;width:170px">Short supporting line for this section of the deck.</p>
    <div class="photo" role="img" aria-label="Two colleagues working at a desk" style="left:220px;top:40px;width:150px;height:110px"></div>
    <div class="photo" role="img" aria-label="Professional on a video call" style="left:380px;top:40px;width:145px;height:110px;background:linear-gradient(135deg,#d9e4ef,#a5bcd6)"></div>
    <div class="team-cards">
      <div class="tcard light"><h5>Title Goes Here</h5><p class="small">Brief text about this point.</p></div>
      <div class="tcard dark"><h5>Title Goes Here</h5><p class="small">Brief text about this point.</p></div>
      <div class="tcard light"><h5>Title Goes Here</h5><p class="small">Brief text about this point.</p></div>
      <div class="tcard light"><h5>Title Goes Here</h5><p class="small">Brief text about this point.</p></div>
    </div>
    <div class="foot"></div>
  </section>

  <!-- Connect -->
  <section class="slide">
    <div class="photo" role="img" aria-label="Team meeting around a table" style="left:0;top:0;bottom:0;width:265px;background:linear-gradient(150deg,#d7c8b6,#9fb3c9)"></div>
    <div class="title" style="left:290px;top:22px;font-size:18px">Connect <span>With Us</span></div>
    <div class="profile">
      <div class="who"><div class="avatar" role="img" aria-label="Portrait photo"></div><div><h4>Sam Porter</h4><p>CEO / Global Management</p></div></div>
      <ul class="contact">
        <li><svg width="10" height="10" viewBox="0 0 10 10"><path d="M2 1l2 2-1 1.5a6 6 0 0 0 2.5 2.5L7 6l2 2-1.5 1.5C4 9 1 6 .5 2.5z" fill="#0094d4"/></svg>+00 000 000 0000</li>
        <li><svg width="10" height="10" viewBox="0 0 10 10"><rect x=".5" y="2" width="9" height="6" fill="none" stroke="#0094d4"/><path d="M.5 2l4.5 3.5L9.5 2" fill="none" stroke="#0094d4"/></svg>sam@veltranhq.com</li>
        <li><svg width="10" height="10" viewBox="0 0 10 10"><circle cx="5" cy="5" r="4" fill="none" stroke="#0094d4"/></svg>veltranhq.com</li>
      </ul>
      <div class="quote">"What I love about this team: they listen, move fast and always bring the right people to the table."</div>
    </div>
    <div class="foot"></div>
  </section>

</main>
</body>
</html>
```